Roll label Flyer design

I need a flyer for a roll label printer
Pictures for the project are located here:
https://plimtonstickers.sharefile.com/d-k4wq7812m3a0z551

Text I want is located here:
https://plimtonstickers.com/roll-labels.php

Target Market(s)

Manufactures, wholesalers

Industry/Entity Type

Printing

Requirements
Must have
• Lots of pictures. Our phone number 800-472-8164. Website www.plimtonstickers.com

```html
<!DOCTYPE html>
<html lang="en">
<head>
<meta charset="utf-8">
<title>Plimton Stickers – Roll/Product Labels Flyer</title>
<link href="https://fonts.googleapis.com/css2?family=Lato:wght@400;700;900&family=Raleway:wght@400;800&display=swap" rel="stylesheet">
<style>
  :root {
    --ink: #2b2d31;
    --ink-deep: #232428;
    --red: #d01f26;
    --red-dark: #b3181e;
    --paper: #ffffff;
    --paper-soft: #f4f4f4;
    --text: #2a2a2a;
    --rule: #c9c9c9;
  }
  * { margin: 0; padding: 0; box-sizing: border-box; }
  html, body { width: 950px; height: 1200px; overflow: hidden; background: var(--paper); }
  .flyer {
    position: relative; width: 950px; height: 1200px; overflow: hidden;
    background: var(--paper-soft);
    font-family: "Lato", sans-serif; color: var(--text);
  }
  .hero { position: absolute; left: 0; top: 0; width: 950px; height: 820px; }
  .brand {
    position: absolute; left: 36px; top: 48px;
    display: flex; align-items: center; gap: 14px;
  }
  .brand-mark { width: 58px; height: 58px; border-radius: 50%; background: var(--red); }
  .brand-name {
    font-family: "Lato", sans-serif; font-weight: 700; font-size: 27px;
    letter-spacing: 6px; color: var(--paper);
  }
  .intro {
    position: absolute; left: 40px; top: 603px; width: 310px;
    color: var(--paper); font-size: 19px; line-height: 25px;
  }
  .title {
    position: absolute; left: 372px; top: 560px;
    font-family: "Raleway", sans-serif; font-size: 54px; color: var(--paper);
    letter-spacing: -0.5px; white-space: nowrap;
  }
  .title strong { font-weight: 800; }
  .title span { font-weight: 400; }
  .details {
    position: absolute; left: 0; top: 820px; width: 950px; height: 304px;
  }
  .col { position: absolute; top: 38px; }
  .col-markets { left: 57px; }
  .col-features { left: 558px; }
  .col h2 { font-size: 26px; font-weight: 400; margin-bottom: 12px; }
  .col h2 strong { color: var(--red); font-weight: 900; }
  .col li {
    list-style: none; font-size: 20px; height: 35px; display: flex; align-items: center; gap: 12px;
  }
  .tick { width: 17px; height: 17px; flex: none; }
  .divider {
    position: absolute; left: 522px; top: 56px; width: 1px; height: 184px; background: var(--rule);
  }
  .footer { position: absolute; left: 0; top: 1124px; width: 950px; height: 76px; }
  .phone {
    position: absolute; left: 36px; top: 0; height: 76px; display: flex; align-items: center; gap: 14px;
    color: var(--paper); font-weight: 900; font-size: 50px;
  }
  .web {
    position: absolute; left: 508px; top: 0; height: 76px; display: flex; align-items: center; gap: 12px;
    color: var(--paper); font-weight: 700; font-size: 26px;
  }
</style>
</head>
<body>
<main class="flyer">

  <section class="hero">
    <svg width="950" height="820" viewBox="0 0 950 820" aria-hidden="false">
      <defs>
        <linearGradient id="photoWarning" x1="0" y1="0" x2="1" y2="1">
          <stop offset="0" stop-color="#5a5650"/><stop offset="0.55" stop-color="#b03a36"/><stop offset="1" stop-color="#3c3a38"/>
        </linearGradient>
        <linearGradient id="photoRoll" x1="0" y1="0" x2="1" y2="0">
          <stop offset="0" stop-color="#d8d6cf"/><stop offset="0.5" stop-color="#2a2a2e"/><stop offset="1" stop-color="#8b8a86"/>
        </linearGradient>
        <linearGradient id="photoFloor" x1="0" y1="0" x2="1" y2="1">
          <stop offset="0" stop-color="#d9d8d2"/><stop offset="0.5" stop-color="#a8a9a6"/><stop offset="1" stop-color="#e4e3de"/>
        </linearGradient>
        <linearGradient id="photoPress" x1="0" y1="0" x2="1" y2="1">
          <stop offset="0" stop-color="#3a3b3e"/><stop offset="0.6" stop-color="#9a9a98"/><stop offset="1" stop-color="#5a4a44"/>
        </linearGradient>
        <linearGradient id="photoRewind" x1="0" y1="0" x2="1" y2="1">
          <stop offset="0" stop-color="#cfcfcc"/><stop offset="1" stop-color="#7b7c7c"/>
        </linearGradient>
      </defs>
      <!-- header and text band -->
      <rect x="0" y="0" width="950" height="820" fill="var(--ink)"/>
      <rect x="0" y="0" width="950" height="135" fill="var(--ink-deep)"/>
      <!-- left photo column -->
      <g role="img" aria-label="Close-up of a roll of red danger warning labels">
        <rect x="3" y="135" width="414" height="195" fill="url(#photoWarning)"/>
      </g>
      <g role="img" aria-label="Close-up of a black printed product label roll on a spindle">
        <polygon points="3,337 384,337 345,542 3,542" fill="url(#photoRoll)"/>
      </g>
      <!-- large factory photo -->
      <g role="img" aria-label="Press operator working at a roll label printing line in the factory">
        <polygon points="462,0 950,0 950,542 351,542 420,337 424,135" fill="url(#photoFloor)"/>
      </g>
      <!-- striped accent -->
      <rect x="5" y="553" width="330" height="12" fill="var(--red)" opacity="0.75"/>
      <!-- title banner -->
      <polygon points="334,549 945,549 945,633 358,633" fill="var(--red)"/>
      <!-- lower photos -->
      <g role="img" aria-label="Printed label web running over a press roller">
        <polygon points="363,642 672,642 722,818 410,818" fill="url(#photoPress)"/>
      </g>
      <g role="img" aria-label="Finished label rolls rewinding on the finishing machine">
        <polygon points="680,642 945,642 945,818 730,818" fill="url(#photoRewind)"/>
      </g>
      <rect x="5" y="815" width="940" height="5" fill="var(--red)"/>
    </svg>

    <div class="brand">
      <span class="brand-mark"></span>
      <span class="brand-name">PLIMTON STICKERS</span>
    </div>

    <h1 class="title"><strong>Roll/Product</strong> <span>Labels</span></h1>

    <p class="intro">Long or short run. Digital or flexographic. Standard shapes or unique, custom diecuts. Simple spot colors or full color with every embellishment. Let us help you create the perfect label for your application.</p>
  </section>

  <section class="details">
    <div class="col col-markets">
      <h2><strong>Specialty Markets</strong> We Service Include:</h2>
      <ul>
        <li><svg class="tick" viewBox="0 0 20 20"><circle cx="10" cy="10" r="10" fill="var(--red)"/><path d="M5.5 10.2l3 3 6-6.2" stroke="#fff" stroke-width="2.4" fill="none"/></svg>Health &amp; Beauty</li>
        <li><svg class="tick" viewBox="0 0 20 20"><circle cx="10" cy="10" r="10" fill="var(--red)"/><path d="M5.5 10.2l3 3 6-6.2" stroke="#fff" stroke-width="2.4" fill="none"/></svg>Food &amp; Beverage</li>
        <li><svg class="tick" viewBox="0 0 20 20"><circle cx="10" cy="10" r="10" fill="var(--red)"/><path d="M5.5 10.2l3 3 6-6.2" stroke="#fff" stroke-width="2.4" fill="none"/></svg>Wine &amp; Spirits</li>
        <li><svg class="tick" viewBox="0 0 20 20"><circle cx="10" cy="10" r="10" fill="var(--red)"/><path d="M5.5 10.2l3 3 6-6.2" stroke="#fff" stroke-width="2.4" fill="none"/></svg>Industrial Safety &amp; Warning</li>
        <li><svg class="tick" viewBox="0 0 20 20"><circle cx="10" cy="10" r="10" fill="var(--red)"/><path d="M5.5 10.2l3 3 6-6.2" stroke="#fff" stroke-width="2.4" fill="none"/></svg>Promotional</li>
        <li><svg class="tick" viewBox="0 0 20 20"><circle cx="10" cy="10" r="10" fill="var(--red)"/><path d="M5.5 10.2l3 3 6-6.2" stroke="#fff" stroke-width="2.4" fill="none"/></svg>Compliance (I.E. UL, CSA, California Prop 65)</li>
      </ul>
    </div>
    <div class="divider"></div>
    <div class="col col-features">
      <h2><strong>Features:</strong></h2>
      <ul>
        <li><svg class="tick" viewBox="0 0 20 20"><circle cx="10" cy="10" r="10" fill="var(--red)"/><path d="M5.5 10.2l3 3 6-6.2" stroke="#fff" stroke-width="2.4" fill="none"/></svg>Foil-Stamping</li>
        <li><svg class="tick" viewBox="0 0 20 20"><circle cx="10" cy="10" r="10" fill="var(--red)"/><path d="M5.5 10.2l3 3 6-6.2" stroke="#fff" stroke-width="2.4" fill="none"/></svg>Embossing</li>
        <li><svg class="tick" viewBox="0 0 20 20"><circle cx="10" cy="10" r="10" fill="var(--red)"/><path d="M5.5 10.2l3 3 6-6.2" stroke="#fff" stroke-width="2.4" fill="none"/></svg>Spot Varnishes</li>
        <li><svg class="tick" viewBox="0 0 20 20"><circle cx="10" cy="10" r="10" fill="var(--red)"/><path d="M5.5 10.2l3 3 6-6.2" stroke="#fff" stroke-width="2.4" fill="none"/></svg>Instant Redeemable Coupons</li>
        <li><svg class="tick" viewBox="0 0 20 20"><circle cx="10" cy="10" r="10" fill="var(--red)"/><path d="M5.5 10.2l3 3 6-6.2" stroke="#fff" stroke-width="2.4" fill="none"/></svg>Expanded Content/Booklet Labels</li>
      </ul>
    </div>
  </section>

  <footer class="footer">
    <svg width="950" height="76" viewBox="0 0 950 76" style="position:absolute;left:0;top:0">
      <rect x="0" y="0" width="950" height="76" fill="var(--ink)"/>
      <polygon points="0,0 494,0 462,76 0,76" fill="var(--red)"/>
      <polygon points="494,0 502,0 470,76 462,76" fill="var(--paper)"/>
    </svg>
    <div class="phone">
      <svg width="36" height="36" viewBox="0 0 36 36"><circle cx="18" cy="18" r="18" fill="var(--paper)"/><path d="M12 9c1-1 2.4-.8 3 .4l1.6 3.2c.4.9.2 1.8-.5 2.4l-1.3 1.1c1 2.3 2.7 4 5 5l1.1-1.3c.6-.7 1.6-.9 2.4-.5l3.2 1.6c1.2.6 1.4 2 .4 3l-1.6 1.6c-1.2 1.2-3 1.5-4.6.8-5-2.2-8.6-5.8-10.8-10.8-.7-1.6-.4-3.4.8-4.6z" fill="var(--red)"/></svg>
      800-472-8164
    </div>
    <div class="web">
      <svg width="24" height="24" viewBox="0 0 24 24" fill="none" stroke="var(--red)" stroke-width="2"><circle cx="12" cy="12" r="10"/><ellipse cx="12" cy="12" rx="4.5" ry="10"/><path d="M2 12h20M4 6.5h16M4 17.5h16"/></svg>
      www.plimtonstickers.com
    </div>
  </footer>

</main>
</body>
</html>
```